Velmora Partners Logo and Business Card Design

We already have the rough logo shape (however please make the lines on the logo much thicker so a dark background is not required to see it) . see photos uploaded.
It needs to be refined with color and digitized and then have a front and back business card layout done.
The services are high vibration healing support through a therapy and feng shui service offering. We want people to Feel Happiness, Feel Prosperity and Feel Peace. (the back of the card would have these phrases on it) So a warm, calm and peaceful feeling card.
We would like the card to use the logo provided (with thicker lines and color added) but below the graphic please use the name "Velmora Partners" NOT Velmora.
We also would like to use the colors in the colorized matrix shown in photos (gold and purple) but on the lighter side. Thanks for your time!

Front of Card should include: Logo, with Company Name: Velmora Partners as part of logo, Name: Dara Pemberton email: dara@velmora-example.me web: www.velmora-example.me mobile: 555.218.4096 at bottom of front list Family Constellation | Feng Shui

Back of Card should have the logo and the following listed vertically:

PERSONAL | BUSINESS (Larger size then smaller bullet items below)
*Find Happiness
*Find Prosperity
*Find Peace

Target Market(s)

Target market is both business and personal

Contact Information for Business Card

Front of Card should include: Logo, with Company Name: Velmora Partners as part of logo, Name: Dara Pemberton email: dara@velmora-example.me web: www.velmora-example.me mobile: 555.218.4096 at bottom of front list Family Constellation | Feng Shui ++++ Back of Card should have the logo and the following listed vertically: PERSONAL | BUSINESS (Larger size then smaller bullet items below) *Find Happiness *Find Prosperity *Find Peace

Font styles to use
Sans Serif

Colors

Designer to choose colors to be used in the design.

Requirements
Nice to have
• Nice light contrast color for the back of card background
Should not have
• No dark colored background on Card.

```html
<!DOCTYPE html>
<html lang="en">
<head>
<meta charset="utf-8">
<title>Velmora Partners – Business Card</title>
<link rel="stylesheet" href="https://fonts.googleapis.com/css2?family=Montserrat:wght@500;600;700&family=Lato:wght@400&display=swap">
<style>
  :root {
    --canvas: #ece7e1;
    --card-white: #ffffff;
    --lavender: #c9b5da;
    --lavender-deco: rgba(255,255,255,0.18);
    --purple: #5a3a93;
    --purple-band: #7b63ad;
    --gold: #d4a62a;
    --gold-light: #ecd04a;
    --gold-deep: #c9961c;
    --ink: #2a2a2a;
  }
  * { margin: 0; padding: 0; box-sizing: border-box; }
  html, body { width: 900px; height: 1200px; overflow: hidden; }
  body { background: var(--canvas); font-family: "Montserrat", sans-serif; position: relative; }

  .card {
    position: absolute; left: 80px; width: 742px; height: 440px;
    border-radius: 32px; overflow: hidden;
    box-shadow: 0 4px 10px rgba(0,0,0,0.18);
  }
  .card--front { top: 132px; background: var(--card-white); }
  .card--back { top: 638px; background: var(--lavender); }

  .deco-ring { position: absolute; border-radius: 50%; }
  .card--front .deco-ring { left: -10px; top: -8px; width: 190px; height: 190px; border: 10px solid #efedf6; }
  .card--back .deco-ring { right: -60px; top: 88px; width: 270px; height: 270px; border: 14px solid var(--lavender-deco); }

  .brand { position: absolute; text-align: center; }
  .brand__mark { width: 84px; height: 84px; border-radius: 50%; border: 7px solid var(--purple); margin: 0 auto 18px; }
  .brand__name { font-weight: 600; color: var(--gold); font-size: 30px; line-height: 1.1; letter-spacing: 1px; }
  .card--front .brand { left: 430px; width: 280px; top: 76px; }
  .card--back .brand { left: 221px; width: 300px; top: 84px; }

  .holder { position: absolute; left: 28px; top: 252px; font-weight: 600; font-size: 24px; color: var(--gold); letter-spacing: 0.5px; text-transform: uppercase; }
  .holder-rule { position: absolute; left: 28px; top: 286px; width: 688px; height: 2px; background: var(--gold-light); }

  .contact { position: absolute; left: 28px; top: 300px; list-style: none; }
  .contact li { display: flex; align-items: center; height: 29px; font-family: "Montserrat", sans-serif; font-weight: 500; font-size: 21px; color: var(--ink); letter-spacing: 0.5px; }
  .contact li:first-child { font-size: 23px; letter-spacing: 1.5px; }
  .contact svg { width: 17px; height: 17px; margin-right: 12px; fill: var(--gold); }

  .footer-bands { position: absolute; left: 0; bottom: 0; width: 742px; height: 58px; }
  .services { position: absolute; right: 24px; bottom: 14px; font-family: "Lato", sans-serif; font-size: 22px; color: var(--ink); word-spacing: 1px; }

  .audience-band {
    position: absolute; left: 0; top: 326px; width: 742px; height: 42px;
    background: linear-gradient(90deg, var(--gold-deep), var(--gold-light) 60%, var(--gold));
    display: flex; align-items: center; justify-content: center;
    font-weight: 700; font-size: 22px; letter-spacing: 1px; color: var(--ink);
  }
  .audience-band span { margin: 0 12px; font-weight: 500; }
  .promises { position: absolute; left: 0; top: 388px; width: 742px; text-align: center; font-family: "Lato", sans-serif; font-size: 22px; color: var(--ink); }
  .promises .dot { display: inline-block; width: 6px; height: 6px; border-radius: 50%; background: var(--gold-light); margin: 0 9px; vertical-align: middle; }
</style>
</head>
<body>

<section class="card card--front" aria-label="Business card front">
  <div class="deco-ring" aria-hidden="true"></div>
  <div class="brand">
    <div class="brand__mark" aria-hidden="true"></div>
    <div class="brand__name">Velmora Partners</div>
  </div>

  <div class="holder">Dara Pemberton</div>
  <div class="holder-rule"></div>

  <ul class="contact">
    <li><svg viewBox="0 0 24 24" aria-hidden="true"><path d="M3 8c0-2 4-4 9-4s9 2 9 4v2h-5V8H8v2H3zM6 11h12l2 8H4z"/></svg>555.218.4096</li>
    <li><svg viewBox="0 0 24 24" aria-hidden="true"><path d="M2 6h20v12H2zM3 7l9 7 9-7v1l-9 7-9-7z"/></svg>dara@velmora-example.me</li>
    <li><svg viewBox="0 0 24 24" aria-hidden="true"><circle cx="12" cy="12" r="10"/></svg>www.velmora-example.me</li>
  </ul>

  <svg class="footer-bands" viewBox="0 0 742 58" aria-hidden="true">
    <defs>
      <linearGradient id="goldBand" x1="0" x2="1" y1="0" y2="0">
        <stop offset="0" stop-color="#ecd04a"/>
        <stop offset="0.7" stop-color="#e6c43e"/>
        <stop offset="1" stop-color="#c9961c"/>
      </linearGradient>
    </defs>
    <path d="M0 16 H320 L304 34 H0 Z" fill="#7b63ad"/>
    <path d="M0 40 H300 Q318 40 326 30 L340 8 Q346 0 360 0 H742 V58 H0 Z" fill="url(#goldBand)"/>
    <path d="M0 34 H304 L300 40 H0 Z" fill="#ffffff"/>
  </svg>
  <div class="services">Family Constellation &nbsp;|&nbsp; Feng Shui</div>
</section>

<section class="card card--back" aria-label="Business card back">
  <div class="deco-ring" aria-hidden="true"></div>
  <div class="brand">
    <div class="brand__mark" aria-hidden="true"></div>
    <div class="brand__name">Velmora Partners</div>
  </div>

  <div class="audience-band">BUSINESS<span>|</span>PERSONAL</div>
  <p class="promises">Find Happiness<span class="dot"></span>Find Prosperity<span class="dot"></span>Find Peace</p>
</section>

</body>
</html>
```